Landing Page / Waitlist

I would like a landing page for people to sign up for a waiting list. The text on the page should include (but is not limited to):
1) Main point: The accounting system you'll love
2) Secondary points:
a. Ruthlessly efficient
b. Quietly intelligent
c. Driven by AI
I've attached a file of our logo

The design should be simple, clean, and innovative - this is an ai company

```html
<!DOCTYPE html>
<html lang="en">
<head>
<meta charset="UTF-8">
<title>LedgerLoom — The Accounting System You'll Love</title>
<link href="https://fonts.googleapis.com/css2?family=Poppins:wght@300;400;500;600&display=swap" rel="stylesheet">
<style>
  :root{
    --bg-deep:#03121c;
    --bg-glow:#0a3a5e;
    --accent:#12a8f5;
    --accent-btn:#0a78d0;
    --text-main:#ffffff;
    --text-soft:#d6e0e8;
    --text-muted:#8a9aa6;
    --field-bg:#f2f3f4;
    --icon-bg:#0b2438;
  }
  *{box-sizing:border-box;margin:0;padding:0}
  html,body{width:1200px;height:939px;overflow:hidden}
  body{
    font-family:"Poppins",sans-serif;
    color:var(--text-main);
    background:radial-gradient(ellipse 620px 560px at 50% 42%,var(--bg-glow) 0%,#072a45 40%,var(--bg-deep) 100%);
    position:relative;
  }
  .brand{
    position:absolute;top:28px;left:0;width:100%;
    display:flex;flex-direction:column;align-items:center;gap:8px;
  }
  .brand-dot{width:30px;height:30px;border-radius:50%;background:var(--accent)}
  .brand-name{font-size:21px;font-weight:500;color:#b8bfc5;letter-spacing:-0.2px}
  .hero{position:absolute;top:187px;left:0;width:100%;text-align:center}
  .eyebrow{font-size:13px;font-weight:300;color:var(--text-muted)}
  .headline{
    font-size:54px;font-weight:600;line-height:64px;letter-spacing:-2.2px;margin-top:6px;
  }
  .headline .highlight{color:var(--accent)}
  .lede{
    font-size:14px;font-weight:300;line-height:23px;color:var(--text-soft);
    width:400px;margin:12px auto 0;
  }
  .signup{
    width:367px;height:49px;margin:26px auto 0;background:var(--field-bg);
    border-radius:25px;display:flex;align-items:center;justify-content:space-between;
    padding:0 6px 0 20px;
  }
  .signup input{
    border:none;background:transparent;font:300 13.5px "Poppins",sans-serif;
    color:#555;outline:none;width:200px;
  }
  .signup input::placeholder{color:#6b6f73}
  .signup button{
    width:132px;height:36px;border:none;border-radius:18px;background:var(--accent-btn);
    color:#fff;font:400 13.5px "Poppins",sans-serif;
  }
  .social-proof{
    display:flex;align-items:center;justify-content:center;gap:7px;margin-top:15px;
    font-size:10.5px;font-weight:400;color:var(--text-soft);
  }
  .avatars{display:flex}
  .avatar{
    width:29px;height:29px;border-radius:50%;border:1.5px solid #fff;margin-left:-8px;
    background:linear-gradient(160deg,#c9a27d,#3a3a42);
  }
  .avatar:first-child{margin-left:0}
  .features{position:absolute;top:617px;left:99px;display:flex}
  .feature{width:349px;display:flex;gap:14px}
  .feature-icon{
    width:32px;height:32px;border-radius:50%;border:1.5px solid var(--accent);
    display:flex;align-items:center;justify-content:center;flex-shrink:0;
  }
  .feature-title{font-size:17.5px;font-weight:400;color:var(--text-soft);line-height:32px}
  .feature-text{
    font-size:13.5px;font-weight:300;line-height:21.7px;color:var(--text-muted);
    margin-top:6px;width:260px;
  }
  .footer{
    position:absolute;top:852px;left:75px;width:1071px;height:34px;
    display:flex;align-items:center;justify-content:space-between;
    font-size:13.5px;font-weight:300;color:var(--text-muted);
  }
  .footer-social{display:flex;gap:11px;position:absolute;left:492px}
  .social-link{
    width:33px;height:33px;border-radius:50%;background:var(--icon-bg);
    display:flex;align-items:center;justify-content:center;
  }
  .footer-links{display:flex;gap:21px}
  .footer-links a{color:var(--text-muted);text-decoration:none}
</style>
</head>
<body>
  <header class="brand">
    <span class="brand-dot"></span>
    <span class="brand-name">LedgerLoom</span>
  </header>

  <main class="hero">
    <p class="eyebrow">AI for Accounting</p>
    <h1 class="headline">The <span class="highlight">Accounting System</span><br>You'll Love</h1>
    <p class="lede">Experience effortless financial management driven by intelligent automation, designed to simplify your workflow.</p>
    <form class="signup">
      <input type="email" placeholder="Your Professional Email">
      <button type="button">Join Waitlist</button>
    </form>
    <div class="social-proof">
      <div class="avatars">
        <span class="avatar" role="img" aria-label="Waitlist member photo"></span>
        <span class="avatar" role="img" aria-label="Waitlist member photo"></span>
        <span class="avatar" role="img" aria-label="Waitlist member photo"></span>
      </div>
      <span>100+ People on the Waitlist</span>
    </div>
  </main>

  <section class="features">
    <article class="feature">
      <span class="feature-icon">
        <svg width="18" height="18" viewBox="0 0 24 24" fill="none" stroke="#12a8f5" stroke-width="2" stroke-linecap="round"><path d="M20 12a8 8 0 1 1-3-6.2"/><path d="M17 2v4h-4"/><path d="M8 13a4 4 0 0 0 8 0"/></svg>
      </span>
      <div>
        <h2 class="feature-title">Ruthlessly Efficient</h2>
        <p class="feature-text">Cut your monthly reconciliation time by up to 80%. Our smart system handles the repetitive tasks, letting you focus on growth.</p>
      </div>
    </article>
    <article class="feature">
      <span class="feature-icon">
        <svg width="18" height="18" viewBox="0 0 24 24" fill="none" stroke="#12a8f5" stroke-width="1.8" stroke-linecap="round"><path d="M12 4v16"/><path d="M12 5a3 3 0 0 0-5 1 3 3 0 0 0-2 5 3 3 0 0 0 1 5 3 3 0 0 0 6 2"/><path d="M12 5a3 3 0 0 1 5 1 3 3 0 0 1 2 5 3 3 0 0 1-1 5 3 3 0 0 1-6 2"/></svg>
      </span>
      <div>
        <h2 class="feature-title">Quietly Intelligent</h2>
        <p class="feature-text">Automated reporting and anomaly detection working 24/7. Get insights without ever needing to run a single manual report.</p>
      </div>
    </article>
    <article class="feature">
      <span class="feature-icon">
        <svg width="18" height="18" viewBox="0 0 24 24" fill="none" stroke="#12a8f5" stroke-width="1.8" stroke-linecap="round"><rect x="6" y="6" width="12" height="12" rx="1.5"/><path d="M9 2v4M15 2v4M9 18v4M15 18v4M2 9h4M2 15h4M18 9h4M18 15h4"/><path d="M9.5 15l1.5-6 1.5 6M10 13h2M14.5 9v6"/></svg>
      </span>
      <div>
        <h2 class="feature-title">Driven by AI</h2>
        <p class="feature-text">Designed by data scientists and financial experts. Future-proof your books with a system that learns and evolves with your business.</p>
      </div>
    </article>
  </section>

  <footer class="footer">
    <span>© 2024 LedgerLoom. All rights reserved.</span>
    <nav class="footer-social">
      <a class="social-link" aria-label="Professional network">
        <svg width="16" height="16" viewBox="0 0 24 24" fill="none" stroke="#12a8f5" stroke-width="2.4" stroke-linecap="round"><path d="M10 14a4 4 0 0 0 5.7 0l3-3a4 4 0 0 0-5.7-5.7l-1 1"/><path d="M14 10a4 4 0 0 0-5.7 0l-3 3a4 4 0 0 0 5.7 5.7l1-1"/></svg>
      </a>
      <a class="social-link" aria-label="Social feed">
        <svg width="16" height="16" viewBox="0 0 24 24" fill="none" stroke="#12a8f5" stroke-width="2.2"><circle cx="18" cy="5" r="2.6"/><circle cx="6" cy="12" r="2.6"/><circle cx="18" cy="19" r="2.6"/><path d="M8.3 10.8l7.4-4.3M8.3 13.2l7.4 4.3"/></svg>
      </a>
      <a class="social-link" aria-label="Email">
        <svg width="17" height="13" viewBox="0 0 20 15" fill="none" stroke="#12a8f5" stroke-width="2" stroke-linejoin="round"><rect x="1" y="1" width="18" height="13" rx="1.5"/><path d="M1.5 2l8.5 6.5L18.5 2"/></svg>
      </a>
    </nav>
    <nav class="footer-links">
      <a href="#">Privacy Policy</a>
      <a href="#">Terms &amp; Conditions</a>
    </nav>
  </footer>
</body>
</html>
```